International gaming entertainment company is looking for an innovative Power Point design *

We are looking for a Power Point design for potential international investors, partners and customers in the gaming industry, meaning that a reference to internationality and gaming should become apparent.
The template should be in a reduced and clear style with a combination of innovation and tradition. It should be adaptive and suitable for various applications (tables, shapes and diagrams).
The color scheme of our company are various shades of gray and burgundy (wine-red), however as for the design in question, we are open to other meaningful suggestions (no garish colors).
Updates

Noch kein Design dabei, dass uns 100%ig überzeugt

Target Market(s)

International investors and partners in the gaming industry

Font styles to use
Serif
Sans Serif
Other font styles liked:
• Interstate

Requirements
Must have
• Clear lines
Modern
Footer line with room for classification (eg Confidential, Public) and page number

```html
<!DOCTYPE html>
<html lang="en">
<head>
<meta charset="utf-8">
<title>Presentation Deck – Meridian Gaming International</title>
<link href="https://fonts.googleapis.com/css2?family=Montserrat:wght@300;800&family=Roboto+Condensed:wght@300;400;700&family=Roboto:wght@300;400;700&display=swap" rel="stylesheet">
<style>
:root{
  --red:#e8202a;
  --wine:#b0121c;
  --ink:#1f1f2e;
  --grey:#c4c4c8;
  --mid:#8d8d93;
  --light:#f0f0f2;
  --rail:#e6e6ea;
  --white:#ffffff;
}
*{box-sizing:border-box;margin:0;padding:0}
html,body{width:1200px;height:2584px;overflow:hidden}
body{position:relative;background:var(--white);font-family:"Roboto",sans-serif;color:var(--ink)}
.stage{position:absolute;left:0;top:0;width:1200px;height:500px;background:var(--light)}
.deck-heading{position:absolute;left:70px;top:182px;font-family:"Montserrat",sans-serif;font-size:62px;line-height:58px;color:var(--ink)}
.deck-heading b{display:block;font-weight:800}
.deck-heading span{display:block;font-weight:300;padding-left:125px}

.slide{position:absolute;width:382px;height:215px;overflow:hidden;background:var(--white)}
.slide.lg{width:470px;height:265px}
.abs{position:absolute}
.rail{position:absolute;left:0;top:0;width:15px;height:100%;background:var(--rail)}
.rail .dot{position:absolute;left:4px;top:7px;width:7px;height:7px;border-radius:50%;background:var(--red)}
.rail .tag{position:absolute;left:-13px;top:150px;width:40px;transform:rotate(-90deg);font-size:3px;letter-spacing:1px;color:var(--mid);text-align:center}
.rail .num{position:absolute;left:3px;bottom:6px;width:9px;height:9px;background:var(--red);color:#fff;font-size:4px;line-height:9px;text-align:center}

.title{font-family:"Roboto Condensed",sans-serif;font-weight:400;font-size:17px;color:var(--ink);white-space:nowrap}
.title.caps{text-transform:uppercase}
.sub{font-size:3.5px;letter-spacing:2px;color:var(--mid);text-transform:uppercase}
.p{font-size:4.2px;line-height:6.4px;color:#55555f}
.p.w{color:#fff}
.red{color:var(--red)}
.mark{width:18px;height:18px;border-radius:50%;background:#fff}
.brand{font-family:"Roboto Condensed",sans-serif;font-weight:700;text-transform:uppercase;letter-spacing:.3px}

.redslide{background:linear-gradient(135deg,#ed2229,#d9161f)}
.redslide .big{font-family:"Roboto Condensed",sans-serif;font-weight:700;color:#fff;white-space:nowrap}
.presented{font-size:3.5px;letter-spacing:2px;color:#fff;text-transform:uppercase}
.presented b{display:block;letter-spacing:0;font-size:4.5px}
.ph{position:absolute}

.pill{border-radius:30px}
.card{position:absolute;width:102px;height:53px;padding:8px 6px 0 36px;box-shadow:0 2px 5px rgba(0,0,0,.12)}
.card.r{background:var(--red);color:#fff}
.card.w{background:#fff}
.card i{position:absolute;left:10px;top:14px;width:20px;height:20px;border-radius:50%;border:1.5px solid currentColor;color:var(--red)}
.card.r i{color:#fff}
.card h5{font-size:4.5px;font-weight:700;margin-bottom:3px}
.card p{font-size:3.6px;line-height:5px}

.tbl{position:absolute;border-collapse:collapse;font-size:4px}
.tbl td{height:16.5px;text-align:center;border-bottom:1px solid #e2e2e5;color:#444}
.tbl td.h{background:var(--red);color:#fff;text-align:left;padding-left:14px;border-bottom:1px solid #ff5a60}
.tbl td.g{background:var(--mid);color:#fff}
.tbl th{font-weight:400;font-size:4px;height:18px;color:#555}
.tbl th.hr{background:var(--red);color:#fff;font-weight:700}

.stat{font-family:"Roboto Condensed",sans-serif;font-size:18px;color:var(--red)}
.lbl{font-size:4px;color:var(--mid);text-align:center;line-height:5.5px}
.tl-tag{position:absolute;width:58px;height:7px;border-radius:4px;font-size:3.6px;color:#fff;padding-left:5px;line-height:7px;font-weight:700}
</style>
</head>
<body>

<section class="stage">
  <h1 class="deck-heading"><b>Presentation</b><span>Deck</span></h1>

  <div class="slide lg redslide" style="left:558px;top:85px">
    <div class="abs mark" style="left:30px;top:54px;width:24px;height:24px"></div>
    <div class="abs big" style="left:30px;top:112px;font-size:31px;line-height:32px">PRESENTATION TITLE</div>
    <div class="abs" style="left:30px;top:146px;font-size:12px;color:#fff;font-family:'Roboto Condensed',sans-serif">Sub title goes here</div>
    <div class="abs presented" style="left:30px;top:200px">Presented by<b>Presenter name</b></div>
  </div>
</section>

<!-- Row 1 -->
<div class="slide redslide" style="left:11px;top:510px">
  <div class="abs mark" style="left:22px;top:42px"></div>
  <div class="abs big" style="left:22px;top:92px;font-size:25px">PRESENTATION TITLE</div>
  <div class="abs" style="left:22px;top:120px;font-size:10px;color:#fff;font-family:'Roboto Condensed',sans-serif">Sub title goes here</div>
  <div class="abs presented" style="left:22px;top:163px">Presented by<b>Presenter name</b></div>
</div>

<div class="slide" style="left:407px;top:510px;background:linear-gradient(160deg,#fafafa,#dcdcdf)" role="img" aria-label="Soft grey architectural photo backdrop">
  <div class="abs brand" style="left:0;width:382px;text-align:center;top:73px;font-size:7px;color:var(--ink)">Meridian Gaming International</div>
  <div class="abs title" style="left:0;width:382px;text-align:center;top:90px;font-size:20px;font-weight:700">Prestation Title Goes Here</div>
  <div class="abs sub red" style="left:0;width:382px;text-align:center;top:117px">Sub title goes here</div>
  <div class="abs" style="left:0;width:382px;text-align:center;top:191px;font-size:3.5px;letter-spacing:2px;color:var(--ink)">PRESENTED BY<br><span class="red" style="letter-spacing:0;font-size:4.5px">Presenter name</span></div>
</div>

<div class="slide" style="left:802px;top:510px">
  <svg class="abs" style="left:0;top:0" width="382" height="215" viewBox="0 0 382 215">
    <defs><linearGradient id="roul" x1="0" y1="0" x2="1" y2="1"><stop offset="0" stop-color="#3a2a1e"/><stop offset=".5" stop-color="#8a2b1f"/><stop offset="1" stop-color="#2d5a3a"/></linearGradient></defs>
    <path d="M190 0 C225 40 215 150 170 215 L382 215 L382 0 Z" fill="var(--red)"/>
    <path d="M208 0 C240 45 232 150 192 215 L382 215 L382 0 Z" fill="url(#roul)" role="img" aria-label="Roulette wheel photo"/>
  </svg>
  <div class="abs brand" style="left:20px;top:48px;font-size:7px">Meridian Gaming International</div>
  <div class="abs title" style="left:20px;top:97px;font-size:20px;font-weight:700">Prestation Title</div>
  <div class="abs title" style="left:20px;top:117px;font-size:17px;font-weight:300">Goes Here</div>
  <div class="abs" style="left:22px;top:190px;font-size:3.5px;letter-spacing:2px">PRESENTED BY<br><span style="letter-spacing:0;font-size:4.5px">Presenter name</span></div>
</div>

<!-- Row 2 -->
<div class="slide" style="left:11px;top:738px">
  <div class="ph" style="left:0;top:0;width:382px;height:115px;background:linear-gradient(180deg,#2a1a14,#6b3a1c 60%,#3b2216)" role="img" aria-label="Photo of a row of slot machines"></div>
  <div class="abs redslide" style="left:0;top:115px;width:382px;height:100px"></div>
  <div class="abs mark" style="left:54px;top:135px;width:16px;height:16px"></div>
  <div class="abs brand" style="left:20px;top:160px;width:88px;text-align:center;font-size:8px;line-height:9px;color:#fff">Meridian Gaming International</div>
  <div class="abs" style="left:129px;top:138px;width:1px;height:50px;background:#fff"></div>
  <div class="abs big" style="left:141px;top:142px;font-size:20px;font-family:'Roboto Condensed',sans-serif;font-weight:700;color:#fff">YOUR SLIDES DECK NAME</div>
  <div class="abs presented" style="left:145px;top:174px">April 20, 2020</div>
</div>

<div class="slide" style="left:407px;top:738px;background:linear-gradient(180deg,#f7f7f8,#ebebee)">
  <div class="abs pill" style="left:71px;top:76px;width:240px;height:52px;background:linear-gradient(90deg,var(--wine),var(--red));box-shadow:0 8px 12px rgba(0,0,0,.18)"></div>
  <div class="abs title" style="left:71px;width:240px;text-align:center;top:90px;color:#fff;font-size:17px;font-weight:400">Here add a shot quote</div>
</div>

<div class="slide" style="left:802px;top:738px">
  <div class="rail"><i class="dot"></i><span class="tag">CONFIDENTIAL</span><span class="num">4</span></div>
  <div class="abs title" style="left:36px;top:22px">Simple Text</div>
  <p class="abs p" style="left:36px;top:62px;width:320px">Lorem ipsum dolor sit amet, consectetur adipiscing elit. Fusce sit amet neque sodales, faucibus ex eu, efficitur lacus. Cras imperdiet, nulla nec sagittis pulvinar, neque augue iaculis risus, ac fringilla felis urna fermentum mi. Ut vehicula vel enim sit amet vulputate. Aenean malesuada consectetur diam, ac convallis quam tincidunt eget. Nam vitae elementum ipsum. Proin vitae blandit enim. Donec congue convallis commodo. Aenean vel lacus lacus. Sed in erat ultrices dolor faucibus feugiat. Nullam cursus sollicitudin dictum.</p>
  <p class="abs p" style="left:36px;top:128px;width:320px">Maecenas in purus at tellus tincidunt sodales eu sed nibh. Aenean justo diam, commodo vel felis ac, malesuada sodales purus. Nunc sollicitudin sed justo in eleifend. Fusce dictum ornare ligula, eu porttitor elit ullamcorper non. Aliquam erat volutpat. Mauris malesuada turpis non tellus scelerisque tempus. Morbi dui turpis, mollis a ultrices blandit, commodo a enim.</p>
</div>

<!-- Row 3 -->
<div class="slide" style="left:11px;top:966px">
  <div class="rail"><i class="dot"></i><span class="tag">CONFIDENTIAL</span><span class="num">7</span></div>
  <div class="abs title" style="left:36px;top:22px">Two Column Text</div>
  <p class="abs p" style="left:36px;top:56px;width:336px">Lorem ipsum dolor sit amet, consectetur adipiscing elit, sed do eiusmod tempor incididunt ut labore et dolore magna aliqua. Lorem ipsum dolor sit amet, consectetur adipiscing elit, sed do eiusmod tempor incididunt ut labore et dolore magna aliqua. Ut enim ad minim veniam, quis nostrud exercitation ullamco laboris nisi ut aliquip.</p>
  <p class="abs p" style="left:36px;top:90px;width:336px">Lorem ipsum dolor sit amet, consectetur adipiscing elit, sed do eiusmod tempor incididunt ut labore et dolore magna aliqua. Lorem ipsum dolor sit amet, consectetur adipiscing elit, sed do eiusmod tempor.</p>
  <div class="abs" style="left:49px;top:122px;width:131px;height:100px;border-radius:12px;background:#cfcfd3"></div>
  <div class="abs" style="left:224px;top:122px;width:131px;height:100px;border-radius:12px;background:var(--red)"></div>
  <p class="abs p w" style="left:64px;top:136px;width:106px">Lorem ipsum dolor sit amet, consectetur adipiscing elit, sed do eiusmod tempor incididunt.</p>
  <p class="abs p w" style="left:238px;top:136px;width:106px">Lorem ipsum dolor sit amet, consectetur adipiscing elit, sed do eiusmod tempor incididunt.</p>
  <p class="abs p w" style="left:64px;top:166px;width:106px">Lorem ipsum is simply dummy printer took a galley of type.</p>
  <p class="abs p w" style="left:238px;top:166px;width:106px">Lorem ipsum is simply dummy printer took a galley of type.</p>
  <p class="abs p w" style="left:64px;top:188px;width:106px">Lorem ipsum is simply dummy printer took a galley of type.</p>
  <p class="abs p w" style="left:238px;top:188px;width:106px">Lorem ipsum is simply dummy printer took a galley of type.</p>
</div>

<div class="slide" style="left:407px;top:966px">
  <div class="rail"><i class="dot"></i><span class="tag">CONFIDENTIAL</span><span class="num">8</span></div>
  <div class="abs title" style="left:36px;top:22px;font-size:13px">Text, Picture and A Quote</div>
  <div class="abs sub" style="left:38px;top:40px">Sub title goes here</div>
  <p class="abs p" style="left:38px;top:58px;width:76px;text-align:justify">Business valuation is a process and a set of procedures used to estimate the economic value of an owner's interest in a business. Valuation is used by financial market participants to determine the price they are willing to pay. In addition to estimating the selling price of a business, the same valuation tools are often used by business appraisers to resolve disputes related to estate and gift taxation.</p>
  <p class="abs p" style="left:126px;top:58px;width:76px;text-align:justify">Business valuation is a process and a set of procedures used to estimate the economic value of an owner's interest in a business. Valuation is used by financial market participants to determine the price they are willing to pay. In addition to estimating the selling price of a business, the same valuation tools are often used by business appraisers to resolve disputes related to estate and gift taxation.</p>
  <div class="ph" style="left:219px;top:24px;width:148px;height:167px;background:radial-gradient(circle at 45% 40%,#e0b866,#7a4a18 45%,#2a1408)" role="img" aria-label="Photo of a golden star"></div>
  <div class="abs" style="left:229px;top:160px;width:153px;height:31px;background:var(--red);padding:6px 8px"><p class="p w">Business valuation is a process and a set of procedures used to estimate the economic value of an owners.</p></div>
</div>

<div class="slide" style="left:802px;top:966px">
  <div class="rail"><i class="dot"></i><span class="tag">CONFIDENTIAL</span><span class="num">9</span></div>
  <div class="ph" style="left:15px;top:0;width:367px;height:215px;background:linear-gradient(120deg,#6a4030,#c98c62 40%,#e8d4c0 65%,#f5f5f5 85%)" role="img" aria-label="Photo of people celebrating at a party"></div>
  <div class="abs" style="left:32px;top:39px;width:141px;height:156px;background:rgba(255,255,255,.94);padding:12px 14px">
    <p class="p">Lorem ipsum dolor sit amet, consectetur adipiscing elit, sed do eiusmod tempor incididunt ut labore et dolore magna aliqua. Lorem ipsum dolor sit amet, consectetur adipiscing elit, sed do eiusmod tempor incididunt ut labore et dolore magna aliqua.</p>
    <p class="p" style="margin-top:8px">Lorem ipsum dolor sit amet, consectetur adipiscing elit, sed do eiusmod tempor. Lorem ipsum dolor sit amet, consectetur adipiscing elit, sed do eiusmod tempor incididunt ut labore et dolore magna aliqua.</p>
  </div>
  <p class="abs p" style="left:182px;top:147px;width:182px">Lorem ipsum dolor sit amet, consectetur adipiscing elit, sed do eiusmod tempor incididunt ut labore et dolore magna aliqua. Lorem ipsum dolor sit amet, consectetur adipiscing elit, sed do eiusmod tempor incididunt ut labore et dolore magna aliqua.</p>
</div>

<!-- Row 4 -->
<div class="slide" style="left:11px;top:1195px">
  <div class="rail"><i class="dot"></i><span class="tag">CONFIDENTIAL</span><span class="num">10</span></div>
  <div class="abs title caps" style="left:34px;top:20px">Group</div>
  <div class="abs" style="left:34px;top:68px;width:12px;height:12px;border-radius:50%;border:3px solid var(--red)"></div>
  <div class="abs" style="left:34px;top:110px;width:12px;height:12px;border-radius:50%;border:3px solid var(--red)"></div>
  <div class="abs" style="left:34px;top:152px;width:12px;height:12px;border-radius:50%;border:3px solid var(--red)"></div>
  <div class="abs" style="left:213px;top:68px;width:12px;height:12px;border-radius:50%;border:3px solid var(--red)"></div>
  <div class="abs" style="left:213px;top:110px;width:12px;height:12px;border-radius:50%;border:3px solid var(--red)"></div>
  <div class="abs" style="left:213px;top:152px;width:12px;height:12px;border-radius:50%;border:3px solid var(--red)"></div>
  <p class="abs p" style="left:56px;top:62px;width:95px"><b>Project name</b><br>Lorem ipsum dolor sit amet, nec an dictas equidem appetere, ut has commune accommodare. Mea illum, iudico.</p>
  <p class="abs p" style="left:56px;top:104px;width:95px"><b>Project name</b><br>Lorem ipsum dolor sit amet, nec an dictas equidem appetere, ut has commune accommodare. Mea illum, iudico.</p>
  <p class="abs p" style="left:56px;top:146px;width:95px"><b>Project name</b><br>Lorem ipsum dolor sit amet, nec an dictas equidem appetere, ut has commune accommodare. Mea illum, iudico.</p>
  <p class="abs p" style="left:234px;top:62px;width:95px"><b>Project name</b><br>Lorem ipsum dolor sit amet, nec an dictas equidem appetere, ut has commune accommodare. Mea illum, iudico.</p>
  <p class="abs p" style="left:234px;top:104px;width:95px"><b>Project name</b><br>Lorem ipsum dolor sit amet, nec an dictas equidem appetere, ut has commune accommodare. Mea illum, iudico.</p>
  <p class="abs p" style="left:234px;top:146px;width:95px"><b>Project name</b><br>Lorem ipsum dolor sit amet, nec an dictas equidem appetere, ut has commune accommodare. Mea illum, iudico.</p>
</div>

<div class="slide" style="left:407px;top:1195px">
  <div class="rail"><i class="dot"></i><span class="tag">CONFIDENTIAL</span><span class="num">11</span></div>
  <div class="abs title" style="left:34px;top:20px">Projects</div>
  <div class="abs sub" style="left:35px;top:40px">Sub title goes here</div>
  <div class="card r" style="left:34px;top:69px"><i></i><h5>Project name</h5><p>Lorem ipsum is simply dummy unknown printer took a galley of type.</p></div>
  <div class="card w" style="left:148px;top:69px"><i></i><h5>Project name</h5><p>Lorem ipsum is simply dummy unknown printer took a galley of type.</p></div>
  <div class="card r" style="left:260px;top:69px"><i></i><h5>Project name</h5><p>Lorem ipsum is simply dummy unknown printer took a galley of type.</p></div>
  <div class="card w" style="left:34px;top:131px"><i></i><h5>Project name</h5><p>Lorem ipsum is simply dummy unknown printer took a galley of type.</p></div>
  <div class="card r" style="left:148px;top:131px"><i></i><h5>Project name</h5><p>Lorem ipsum is simply dummy unknown printer took a galley of type.</p></div>
  <div class="card w" style="left:260px;top:131px"><i></i><h5>Project name</h5><p>Lorem ipsum is simply dummy unknown printer took a galley of type.</p></div>
</div>

<div class="slide" style="left:802px;top:1195px">
  <div class="rail"><i class="dot"></i><span class="tag">CONFIDENTIAL</span><span class="num">12</span></div>
  <div class="abs title" style="left:35px;top:22px">Text and Two Pictures</div>
  <div class="abs sub" style="left:36px;top:42px">Sub title goes here</div>
  <p class="abs p" style="left:38px;top:82px;width:70px">Lorem Ipsum is simply dummy text of the printing and typesetting industry. Lorem Ipsum has been the industry's standard dummy text ever since the 1500s, when an unknown printer took a galley of type and scrambled it to make a type specimen book.</p>
  <div class="ph" style="left:126px;top:63px;width:118px;height:99px;background:linear-gradient(180deg,#1b2f52,#3b5a3a 65%,#8a8a8a)" role="img" aria-label="Photo of a building at dusk"></div>
  <div class="ph" style="left:249px;top:63px;width:119px;height:99px;background:radial-gradient(circle at 60% 45%,var(--red) 25%,#8a4a2a 50%,#5a3018)" role="img" aria-label="Photo of a product on a wooden surface"></div>
  <div class="abs" style="left:126px;top:162px;width:118px;height:24px;background:var(--red);color:#fff;font-size:5px;font-weight:700;text-align:center;line-height:24px">Your Title Here</div>
  <div class="abs" style="left:249px;top:162px;width:119px;height:24px;background:#b5b5ba;color:#fff;font-size:5px;font-weight:700;text-align:center;line-height:24px">Your Title Here</div>
</div>

<!-- Row 5 -->
<div class="slide" style="left:11px;top:1424px">
  <div class="rail"><i class="dot"></i><span class="tag">CONFIDENTIAL</span><span class="num">13</span></div>
  <div class="abs title caps" style="left:34px;top:20px;font-weight:700;font-size:15px">The Meridian Gaming Group</div>
  <div class="abs" style="left:29px;top:70px;width:84px;height:14px;background:var(--red);color:#fff;font-size:4.5px;font-weight:700;text-align:center;line-height:14px">PLAYNET</div>
  <div class="abs" style="left:115px;top:70px;width:84px;height:14px;background:var(--red);color:#fff;font-size:4.5px;font-weight:700;text-align:center;line-height:14px">NATIONAL LOTTO</div>
  <div class="abs" style="left:203px;top:70px;width:84px;height:14px;background:var(--red);color:#fff;font-size:4.5px;font-weight:700;text-align:center;line-height:14px">LUCKYHALL</div>
  <div class="abs" style="left:291px;top:70px;width:84px;height:14px;background:var(--red);color:#fff;font-size:4.5px;font-weight:700;text-align:center;line-height:14px">SCOREBET</div>
  <div class="ph" style="left:29px;top:84px;width:84px;height:72px;background:linear-gradient(160deg,#9a9aa6,#5a6a8a)" role="img" aria-label="Photo of a hand holding a tablet with a game"></div>
  <div class="ph" style="left:115px;top:84px;width:84px;height:72px;background:linear-gradient(160deg,#d8a040,#b0302a 60%,#3a6a3a)" role="img" aria-label="Photo of colourful lottery tickets"></div>
  <div class="ph" style="left:203px;top:84px;width:84px;height:72px;background:linear-gradient(160deg,#5a2a1a,#b06a30 55%,#3a2a24)" role="img" aria-label="Photo of a gaming hall interior"></div>
  <div class="ph" style="left:291px;top:84px;width:84px;height:72px;background:linear-gradient(160deg,#3a6a3a,#8ab05a 55%,#2a4a2a)" role="img" aria-label="Photo of a phone showing a betting app"></div>
  <p class="abs p" style="left:29px;top:160px;width:84px;text-align:center">Lorem ipsum dolor sit amet, nec an dictas equidem appetere, ut has commune.</p>
  <p class="abs p" style="left:115px;top:160px;width:84px;text-align:center">Lorem ipsum dolor sit amet, nec an dictas equidem appetere, ut has commune.</p>
  <p class="abs p" style="left:203px;top:160px;width:84px;text-align:center">Lorem ipsum dolor sit amet, nec an dictas equidem appetere, ut has commune.</p>
  <p class="abs p" style="left:291px;top:160px;width:84px;text-align:center">Lorem ipsum dolor sit amet, nec an dictas equidem appetere, ut has commune.</p>
</div>

<div class="slide" style="left:407px;top:1424px">
  <div class="rail"><i class="dot"></i><span class="tag">CONFIDENTIAL</span><span class="num">14</span></div>
  <div class="abs title" style="left:34px;top:20px">Inforaphic</div>
  <div class="abs sub" style="left:35px;top:38px">Sub title goes here</div>
  <svg class="abs" style="left:132px;top:62px" width="130" height="130" viewBox="0 0 130 130">
    <g fill="none" stroke-width="22">
      <circle cx="65" cy="65" r="50" stroke="#d2d2d6" stroke-dasharray="50 4.4" transform="rotate(-90 65 65)"/>
      <path d="M65 15 A50 50 0 0 1 108 40" stroke="var(--red)"/>
      <path d="M22 90 A50 50 0 0 0 65 115" stroke="#a5a5ab"/>
    </g>
    <circle cx="65" cy="65" r="28" fill="#fff" stroke="#e3e3e6" stroke-width="2"/>
    <circle cx="65" cy="65" r="12" fill="var(--red)"/>
  </svg>
  <p class="abs p" style="left:40px;top:62px;width:90px;text-align:center"><b>Lorem ipsum dolor</b><br>Lorem ipsum dolor sit amet, consectetur adipiscing elit, sed do eiusmod tempor</p>
  <p class="abs p" style="left:30px;top:116px;width:90px;text-align:center"><b>Lorem ipsum dolor</b><br>Lorem ipsum dolor sit amet, consectetur adipiscing elit, sed do eiusmod tempor</p>
  <p class="abs p" style="left:46px;top:170px;width:90px;text-align:center"><b>Lorem ipsum dolor</b><br>Lorem ipsum dolor sit amet, consectetur adipiscing elit, sed do eiusmod tempor</p>
  <p class="abs p" style="left:252px;top:60px;width:100px"><b>Lorem ipsum dolor</b><br>Lorem ipsum dolor sit amet, consectetur adipiscing elit, sed do eiusmod tempor</p>
  <p class="abs p" style="left:274px;top:114px;width:96px"><b>Lorem ipsum dolor</b><br>Lorem ipsum dolor sit amet, consectetur adipiscing elit, sed do eiusmod tempor</p>
  <p class="abs p" style="left:256px;top:168px;width:100px"><b>Lorem ipsum dolor</b><br>Lorem ipsum dolor sit amet, consectetur adipiscing elit, sed do eiusmod tempor</p>
</div>

<div class="slide" style="left:802px;top:1424px">
  <div class="rail"><i class="dot"></i><span class="tag">CONFIDENTIAL</span><span class="num">15</span></div>
  <div class="abs title" style="left:15px;width:367px;text-align:center;top:45px;font-weight:700;font-size:18px">Your <span class="red">Awesome</span> text here</div>
  <svg class="abs" style="left:122px;top:95px" width="124" height="66" viewBox="0 0 124 66">
    <path d="M2 33 L26 8 V22 H58 V44 H26 V58 Z" fill="#a5a5ab"/>
    <path d="M122 33 L98 8 V22 H66 V44 H98 V58 Z" fill="var(--red)"/>
    <circle cx="62" cy="33" r="22" fill="#fff" stroke="#e3e3e6"/>
    <circle cx="62" cy="33" r="9" fill="var(--red)"/>
  </svg>
  <p class="abs p" style="left:34px;top:90px;width:88px"><b>Lorem ipsum dolor</b><br>Lorem ipsum dolor sit amet, consectetur adipiscing elit, sed do eiusmod tempor</p>
  <p class="abs p" style="left:42px;top:122px;width:80px">› Lorem ipsum dolor<br>› Sit amet consectetur adipiscing<br>› Do eiusmod tempor<br>› Ut perspiciatis<br>› Lorem ipsum dolor</p>
  <p class="abs p" style="left:284px;top:90px;width:88px"><b>Lorem ipsum dolor</b><br>Lorem ipsum dolor sit amet, consectetur adipiscing elit, sed do eiusmod tempor</p>
  <p class="abs p" style="left:284px;top:122px;width:80px">› Lorem ipsum dolor<br>› Sit amet consectetur adipiscing<br>› Do eiusmod tempor<br>› Ut perspiciatis<br>› Lorem ipsum dolor</p>
</div>

<!-- Row 6 -->
<div class="slide" style="left:11px;top:1652px;background:linear-gradient(160deg,#fff 40%,#f1f1f3)">
  <div class="rail"><i class="dot"></i><span class="tag">CONFIDENTIAL</span><span class="num">16</span></div>
  <div class="abs title" style="left:34px;top:40px;font-size:16px;line-height:21px;white-space:normal;width:140px">Here add some short text to <span class="red">explain some things</span></div>
  <div class="abs" style="left:198px;top:104px;font-family:'Roboto Condensed',sans-serif;font-size:28px;color:var(--red)">56%</div>
  <p class="abs p" style="left:257px;top:96px;width:105px;font-size:4.6px;line-height:8px">Lorem ipsum dolor sit amet. Etiam et hac palta consectetur adipiscing elit.</p>
  <p class="abs p" style="left:198px;top:128px;width:164px;font-size:4.6px;line-height:8px">Fusce sit amet neque iaculis sodales ex eu, efficitur lacus. Cras imperdiet, nulla nec sagittis pulvinar, neque augue iaculis risus, ac fringilla felis urna fermentum mi. Ut vehicula vel enim sit amet vulputate.</p>
</div>

<div class="slide" style="left:407px;top:1652px">
  <div class="rail"><i class="dot"></i><span class="tag">CONFIDENTIAL</span><span class="num">17</span></div>
  <div class="abs title" style="left:15px;width:367px;text-align:center;top:44px;font-weight:700;font-size:18px">Your <span class="red">awesome</span> text here</div>
  <p class="abs p" style="left:44px;top:70px;width:294px;text-align:center">Lorem Ipsum the printing and typesetting industry. Lorem Ipsum has been the industry's standard dummy text ever since the 1500s, when an unknown printer took a galley of type and scrambled it to make a type specimen book. It has survived not only five centuries.</p>
  <div class="abs stat" style="left:44px;width:86px;text-align:center;top:120px">1M</div>
  <div class="abs stat" style="left:148px;width:86px;text-align:center;top:120px">2021</div>
  <div class="abs stat" style="left:254px;width:86px;text-align:center;top:120px">150+</div>
  <div class="abs" style="left:137px;top:118px;width:1px;height:50px;background:#e0e0e3"></div>
  <div class="abs" style="left:246px;top:118px;width:1px;height:50px;background:#e0e0e3"></div>
  <p class="abs lbl" style="left:40px;width:94px;top:148px">Lorem Ipsum has been the industry's standard dummy text ever since the 1500s</p>
  <p class="abs lbl" style="left:144px;width:94px;top:148px">Lorem Ipsum has been the industry's standard dummy text ever since</p>
  <p class="abs lbl" style="left:250px;width:94px;top:148px">Lorem Ipsum has been the industry's standard dummy text ever since the 1500s</p>
</div>

<div class="slide" style="left:802px;top:1652px">
  <div class="rail"><i class="dot"></i><span class="tag">CONFIDENTIAL</span><span class="num">18</span></div>
  <svg class="abs" style="left:40px;top:60px" width="160" height="125" viewBox="0 0 160 125">
    <g font-size="4" fill="#555" font-family="Roboto,sans-serif">
      <line x1="0" y1="100" x2="158" y2="100" stroke="#ddd"/>
      <rect x="8" y="24" width="6" height="76" fill="var(--red)"/><rect x="16" y="58" width="6" height="42" fill="#a5a5ab"/><rect x="24" y="64" width="6" height="36" fill="#d2d2d6"/>
      <text x="6" y="21">4.3</text><text x="15" y="55">2.4</text><text x="24" y="61">2</text>
      <rect x="48" y="22" width="6" height="78" fill="var(--red)"/><rect x="56" y="56" width="6" height="44" fill="#a5a5ab"/><rect x="64" y="64" width="6" height="36" fill="#d2d2d6"/>
      <text x="46" y="19">4.4</text><text x="55" y="53">2.5</text><text x="64" y="61">2</text>
      <rect x="88" y="38" width="6" height="62" fill="var(--red)"/><rect x="96" y="68" width="6" height="32" fill="#a5a5ab"/><rect x="104" y="47" width="6" height="53" fill="#d2d2d6"/>
      <text x="86" y="35">3.5</text><text x="95" y="65">1.8</text><text x="104" y="44">3</text>
      <rect x="128" y="20" width="6" height="80" fill="var(--red)"/><rect x="136" y="68" width="6" height="32" fill="#a5a5ab"/><rect x="144" y="12" width="6" height="88" fill="#d2d2d6"/>
      <text x="126" y="17">4.5</text><text x="135" y="65">1.8</text><text x="145" y="9">5</text>
      <text x="4" y="110">Category 1</text><text x="44" y="110">Category 2</text><text x="84" y="110">Category 3</text><text x="124" y="110">Category 4</text>
    </g>
  </svg>
  <div class="abs" style="left:210px;top:41px;width:155px;height:143px;border:1px solid #e6e6e9;border-radius:10px;background:#fff"></div>
  <div class="abs title" style="left:229px;top:50px;font-weight:700;font-size:17px">Chart</div>
  <div class="abs" style="left:229px;top:70px;font-size:6px;color:#555">Lorem ipsum dolor sit amet</div>
  <div class="abs" style="left:229px;top:90px;font-family:'Roboto Condensed',sans-serif;font-size:19px;color:var(--red)">35 %</div>
  <p class="abs p" style="left:280px;top:98px;width:75px">Lorem ipsum dolor sit amet,</p>
  <p class="abs p" style="left:229px;top:114px;width:125px">consectetur adipiscing elit, sed do eiusmod tempor incididunt ut labore et dolore magna aliqua.</p>
  <p class="abs p" style="left:232px;top:132px;width:122px">› Lorem ipsum dolor sit amet, consectetur adipiscing elit, sed do eiusmod tempor incididunt ut labore et dolore magna aliqua.</p>
  <p class="abs p" style="left:232px;top:158px;width:122px">› Lorem ipsum dolor sit amet, consectetur adipiscing elit.</p>
</div>

<!-- Row 7 -->
<div class="slide" style="left:11px;top:1881px">
  <div class="rail"><i class="dot"></i><span class="tag">CONFIDENTIAL</span><span class="num">19</span></div>
  <div class="abs title" style="left:34px;top:20px;font-weight:700;font-size:15px">Statistic</div>
  <div class="abs sub" style="left:35px;top:38px">Sub title goes here</div>
  <p class="abs p" style="left:44px;top:48px;width:300px;text-align:center">Lorem ipsum the printing and typesetting industry. Lorem ipsum has been the industry's standard dummy text ever since the 1500s, when an unknown printer took a galley of type and scrambled it to make a type specimen book. It has survived not only five centuries.</p>
  <svg class="abs" style="left:58px;top:89px" width="280" height="72" viewBox="0 0 280 72">
    <g fill="none" stroke-width="5">
      <circle cx="36" cy="36" r="30" stroke="#ececef"/>
      <circle cx="36" cy="36" r="30" stroke="#ececef"/>
      <circle cx="132" cy="36" r="30" stroke="#ececef"/>
      <circle cx="132" cy="36" r="30" stroke="var(--red)" stroke-dasharray="141.4 188.5" transform="rotate(-90 132 36)"/>
      <circle cx="228" cy="36" r="30" stroke="#ececef"/>
      <circle cx="228" cy="36" r="30" stroke="#a5a5ab" stroke-dasharray="75.4 188.5" transform="rotate(-90 228 36)"/>
    </g>
    <g font-family="Roboto Condensed,sans-serif" font-size="14" fill="var(--ink)" text-anchor="middle">
      <text x="36" y="41">50%</text><text x="132" y="41">75%</text><text x="228" y="41">40%</text>
    </g>
  </svg>
  <p class="abs lbl" style="left:60px;width:72px;top:170px">Lorem ipsum dolor amet amet consectetur dolor</p>
  <p class="abs lbl" style="left:155px;width:72px;top:170px">Lorem ipsum dolor amet amet consectetur dolor</p>
  <p class="abs lbl" style="left:251px;width:72px;top:170px">Lorem ipsum dolor amet amet consectetur dolor</p>
</div>

<div class="slide" style="left:407px;top:1881px">
  <div class="rail"><i class="dot"></i><span class="tag">CONFIDENTIAL</span><span class="num">20</span></div>
  <div class="abs title" style="left:34px;top:20px;font-weight:700;font-size:15px">Table Of Content</div>
  <div class="abs sub" style="left:35px;top:38px">Sub title goes here</div>
  <div class="abs" style="left:34px;top:54px;width:330px;height:146px;box-shadow:0 2px 6px rgba(0,0,0,.12);border-radius:4px"></div>
  <table class="tbl" style="left:40px;top:58px;width:318px">
    <tr><th style="width:90px"></th><th>You can replace this text.</th><th>You can replace this text.</th><th>You can replace this text.</th><th>You can replace this text.</th></tr>
    <tr><td class="h">You can replace this text</td><td class="g">✓</td><td>×</td><td>×</td><td>×</td></tr>
    <tr><td class="h">You can replace this text</td><td class="g">✓</td><td>×</td><td>×</td><td>×</td></tr>
    <tr><td class="h">You can replace this text</td><td class="g">✓</td><td>×</td><td>×</td><td>×</td></tr>
    <tr><td class="h">You can replace this text</td><td class="g">✓</td><td>×</td><td>×</td><td>×</td></tr>
    <tr><td class="h">You can replace this text</td><td class="g">✓</td><td>×</td><td>×</td><td>×</td></tr>
    <tr><td class="h">You can replace this text</td><td class="g"></td><td></td><td></td><td></td></tr>
  </table>
</div>

<div class="slide" style="left:802px;top:1881px">
  <div class="rail"><i class="dot"></i><span class="tag">CONFIDENTIAL</span><span class="num">21</span></div>
  <div class="abs title" style="left:34px;top:20px;font-weight:700;font-size:15px">Table Of Content</div>
  <div class="abs sub" style="left:35px;top:38px">Sub title goes here</div>
  <div class="abs" style="left:32px;top:54px;width:337px;height:148px;box-shadow:0 2px 6px rgba(0,0,0,.12);border-radius:4px"></div>
  <table class="tbl" style="left:38px;top:68px;width:326px">
    <tr><th style="width:90px"></th><th class="hr">You can replace this text</th><th class="hr">You can replace this text</th><th class="hr">You can replace this text</th><th class="hr">You can replace this text</th><th class="hr">You can replace this text</th></tr>
    <tr><td style="text-align:left;padding-left:14px">You can replace this text</td><td>23</td><td>45</td><td>4</td><td>4</td><td>34</td></tr>
    <tr><td style="text-align:left;padding-left:14px">You can replace this text</td><td>234</td><td>75</td><td>4</td><td>4</td><td>66</td></tr>
    <tr><td style="text-align:left;padding-left:14px">You can replace this text</td><td>55</td><td>75</td><td>64</td><td>6</td><td>44</td></tr>
    <tr><td style="text-align:left;padding-left:14px">You can replace this text</td><td>66</td><td>45</td><td>4</td><td>4</td><td>44</td></tr>
    <tr><td style="text-align:left;padding-left:14px">You can replace this text</td><td>78</td><td>64</td><td>46</td><td>6</td><td>34</td></tr>
    <tr><td style="text-align:left;padding-left:14px">You can replace this text</td><td>56</td><td>46</td><td>44</td><td>3</td><td>55</td></tr>
  </table>
</div>

<!-- Row 8 -->
<div class="slide" style="left:11px;top:2109px">
  <div class="rail"><i class="dot"></i><span class="tag">CONFIDENTIAL</span><span class="num">22</span></div>
  <div class="abs title" style="left:35px;top:20px;font-weight:700;font-size:15px">Our Executive Board</div>
  <div class="abs" style="left:30px;top:60px;width:150px;height:128px;border-radius:40px 14px 40px 14px;background:#dcdce0"></div>
  <div class="abs" style="left:206px;top:56px;width:150px;height:128px;border-radius:14px 40px 14px 40px;background:#dcdce0"></div>
  <p class="abs p" style="left:44px;top:72px;width:122px;text-align:center">Daniel Hartmann studied Business Administration and has worked in the gaming industry for many years. He has held several management positions in operations, finance and strategy, and now leads the international group as chief executive.</p>
  <p class="abs p" style="left:220px;top:68px;width:122px;text-align:center">Martin Keller is an experienced professional who has spent more than twenty years in the gaming sector. After roles in hospitality and controlling he joined the group board, where he now directs daily operations across all international venues.</p>
  <div class="ph" style="left:38px;top:156px;width:34px;height:34px;border-radius:50%;background:linear-gradient(180deg,#b5b5ba,#55555f)" role="img" aria-label="Portrait of the chief executive officer"></div>
  <div class="ph" style="left:214px;top:152px;width:34px;height:34px;border-radius:50%;background:linear-gradient(180deg,#b5b5ba,#55555f)" role="img" aria-label="Portrait of the chief operating officer"></div>
  <div class="abs" style="left:78px;top:162px;font-size:5px;line-height:7px"><span class="red" style="font-family:'Roboto Condensed',sans-serif">Daniel Hartmann</span><br>Chief Executive Officer</div>
  <div class="abs" style="left:255px;top:158px;font-size:5px;line-height:7px"><span class="red" style="font-family:'Roboto Condensed',sans-serif">Martin Keller</span><br>Chief Operating Officer</div>
</div>

<div class="slide" style="left:407px;top:2109px;background:#e9e9ec">
  <div class="rail"><i class="dot"></i><span class="tag">CONFIDENTIAL</span><span class="num">23</span></div>
  <div class="abs title caps" style="left:27px;top:16px;font-weight:700;font-size:14px">Meridian Gaming International</div>
  <div class="abs sub" style="left:27px;top:33px">A global player</div>
  <div class="ph" style="left:50px;top:52px;width:300px;height:150px;border-radius:40px;background:radial-gradient(ellipse at 50% 50%,#f7f7f9 40%,#e9e9ec 75%)" role="img" aria-label="World map with red location pins"></div>
</div>

<div class="slide" style="left:802px;top:2109px">
  <div class="rail"><i class="dot"></i><span class="tag">CONFIDENTIAL</span><span class="num">24</span></div>
  <div class="abs title" style="left:15px;width:367px;text-align:center;top:22px;font-size:14px;font-weight:700">Your Company <span class="red">Timeline</span></div>
  <svg class="abs" style="left:15px;top:40px" width="367" height="175" viewBox="0 0 367 175">
    <path d="M0 28 H330 A30 30 0 0 1 330 88 H40 A30 30 0 0 0 40 148 H367" fill="none" stroke="#d2d2d6" stroke-width="1.2"/>
    <g fill="var(--red)"><circle cx="72" cy="28" r="2.5"/><circle cx="162" cy="28" r="2.5" fill="#a5a5ab"/><circle cx="252" cy="28" r="2.5"/><circle cx="72" cy="88" r="2.5"/><circle cx="162" cy="88" r="2.5"/><circle cx="252" cy="88" r="2.5" fill="#a5a5ab"/></g>
  </svg>
  <div class="tl-tag" style="left:74px;top:71px;background:var(--red)">Project name</div>
  <div class="tl-tag" style="left:164px;top:71px;background:#a5a5ab">Project name</div>
  <div class="tl-tag" style="left:254px;top:71px;background:var(--red)">Project name</div>
  <div class="tl-tag" style="left:74px;top:131px;background:#a5a5ab">Project name</div>
  <div class="tl-tag" style="left:164px;top:131px;background:var(--red)">Project name</div>
  <div class="tl-tag" style="left:254px;top:131px;background:#a5a5ab">Project name</div>
  <p class="abs p" style="left:78px;top:81px;width:60px">Lorem Ipsum is simply dummy unknown printer took a galley of type.</p>
  <p class="abs p" style="left:168px;top:81px;width:60px">Lorem Ipsum is simply dummy unknown printer took a galley of type.</p>
  <p class="abs p" style="left:258px;top:81px;width:60px">Lorem Ipsum is simply dummy unknown printer took a galley of type.</p>
  <p class="abs p" style="left:78px;top:141px;width:60px">Lorem Ipsum is simply dummy unknown printer took a galley of type.</p>
  <p class="abs p" style="left:168px;top:141px;width:60px">Lorem Ipsum is simply dummy unknown printer took a galley of type.</p>
  <p class="abs p" style="left:258px;top:141px;width:60px">Lorem Ipsum is simply dummy unknown printer took a galley of type.</p>
</div>

<!-- Row 9 -->
<div class="slide redslide" style="left:216px;top:2337px">
  <div class="abs mark" style="left:344px;top:122px;width:22px;height:22px"></div>
  <div class="abs big" style="left:0;width:367px;text-align:right;top:148px;font-size:25px">Page break</div>
  <div class="abs" style="left:0;top:179px;width:290px;height:1px;background:#fff"></div>
  <div class="abs" style="left:0;width:367px;text-align:right;top:181px;font-size:9px;color:#fff;font-family:'Roboto Condensed',sans-serif">Sub title goes here</div>
</div>

<div class="slide" style="left:611px;top:2337px;background:#dcdce0">
  <div class="abs" style="left:70px;top:40px;width:7px;height:7px;background:#55555f"></div>
  <div class="abs" style="left:80px;top:40px;width:7px;height:7px;background:#55555f"></div>
  <div class="abs" style="left:90px;top:40px;width:7px;height:7px;background:#55555f"></div>
  <div class="abs" style="left:100px;top:40px;width:7px;height:7px;background:#55555f"></div>
  <div class="abs" style="left:40px;top:55px;width:102px;height:110px;background:#fff;box-shadow:0 2px 6px rgba(0,0,0,.1)"></div>
  <div class="abs" style="left:40px;top:55px;width:102px;height:27px;background:var(--red)"></div>
  <svg class="abs" style="left:48px;top:63px" width="12" height="96" viewBox="0 0 12 96">
    <circle cx="6" cy="6" r="4.5" fill="none" stroke="#fff"/><path d="M1.5 6 H10.5 M6 1.5 V10.5" stroke="#fff" stroke-width=".6"/>
    <path d="M6 42 C2 36 2 30 6 30 C10 30 10 36 6 42 Z" fill="none" stroke="var(--red)"/>
    <path d="M2 56 L4 54 L6 57 L5 58 C6 60 7 61 8 61 L9 60 L12 62 L10 64 C5 63 2 60 2 56 Z" fill="var(--red)"/>
    <rect x="1" y="84" width="10" height="7" fill="var(--red)"/><path d="M1 84 L6 88 L11 84" stroke="#fff" fill="none" stroke-width=".6"/>
  </svg>
  <div class="abs" style="left:66px;top:66px;font-size:4.5px;color:#fff">www.example.com</div>
  <div class="abs" style="left:66px;top:93px;font-size:4.5px;color:#555;line-height:6px">Here to write your<br>Company adress</div>
  <div class="abs" style="left:66px;top:120px;font-size:4.5px;color:#555">(555) 010-2505</div>
  <div class="abs" style="left:66px;top:148px;font-size:4.5px;color:#555">info@example.com</div>
  <div class="abs" style="left:252px;top:80px;width:26px;height:26px;border-radius:50%;background:var(--red)"></div>
  <div class="abs" style="left:165px;width:200px;text-align:center;top:112px;font-family:'Roboto Condensed',sans-serif;font-size:30px;color:#a5a5ab;letter-spacing:1px">THANK YOU</div>
</div>

</body>
</html>
```